QVLT Meridian LLC Website

Basic website for a start up business in the defense and federal space. If we could have intelligence analysis and technology as a focus that would be great. Looking to use our core colors but a lighter set of web pages would be preferable

Target Market(s)

Defense

Coding

Coded - Design and coding required

Number of Pages Required

3 page

```html
<!DOCTYPE html>
<html lang="en">
<head>
<meta charset="utf-8">
<title>QVLT Meridian LLC — Intelligence Analysis and Technology</title>
<link href="https://fonts.googleapis.com/css2?family=Syncopate:wght@400;700&family=Roboto:wght@300;400;500;700&display=swap" rel="stylesheet">
<style>
:root{
  --red:#c4082f;
  --red-deep:#a8001f;
  --ink:#151515;
  --text:#444;
  --muted:#8a8a8a;
  --light:#f3f4f9;
  --grey-band:#eceef2;
  --footer:#1e1f21;
  --footer-bottom:#141516;
  --white:#fff;
}
*{margin:0;padding:0;box-sizing:border-box}
html,body{width:1200px;height:3866px;overflow:hidden}
body{position:relative;background:var(--white);font-family:"Roboto",Arial,sans-serif;color:var(--text)}
.backdrop{position:absolute;left:0;top:0;width:1200px;height:3866px;z-index:0}
.abs{position:absolute;z-index:1}
.display{font-family:"Syncopate","Arial Black",sans-serif;text-transform:uppercase;letter-spacing:1px;line-height:1.05}
.display b{font-weight:700}
.display span{font-weight:400}
.rule{width:52px;height:3px;background:var(--red)}
.para{font-size:14px;line-height:23px;color:var(--text)}
.btn{display:flex;align-items:center;justify-content:center;border-radius:24px;font-size:13px;font-weight:700;text-transform:uppercase;text-decoration:none}
.btn-solid{background:var(--red);color:var(--white)}
.btn-outline{border:2px solid var(--red);color:var(--red);background:transparent}
.btn-ghost{border:2px solid var(--white);color:var(--white)}
.art{border-radius:18px}

/* header */
.brand{left:120px;top:30px;font-family:"Syncopate",sans-serif;font-weight:700;font-size:22px;color:var(--ink);letter-spacing:1px}
.nav{left:358px;top:38px;display:flex;gap:0}
.nav a{font-size:13px;color:#555;text-decoration:none;text-transform:uppercase;width:130px}
.nav a.active{color:var(--ink);font-weight:700}
.nav-cta{left:955px;top:27px;width:132px;height:40px;font-size:13px}
.arrow{width:22px;height:40px;color:#fff;font-size:34px;font-weight:300}

/* features */
.feature{display:flex;gap:12px;width:300px}
.feature .icon{flex:0 0 74px;height:74px;border-radius:50%}
.feature h4{font-size:14px;font-weight:500;color:#222;margin-top:14px;text-transform:uppercase}
.feature p{font-size:11.5px;line-height:17px;color:#555;margin-top:4px}

/* contact */
.contact-item{display:flex;align-items:center;gap:14px}
.contact-item .ring{width:66px;height:66px;border-radius:50%;border:2px solid #e4e4e4;display:flex;align-items:center;justify-content:center;background:#fff}
.contact-item small{display:block;font-size:13px;color:#333}
.contact-item strong{font-weight:400;font-size:16px;color:#222}
.form{left:584px;top:3008px;width:488px;height:379px;border:2px solid var(--red);border-radius:6px;background:var(--white)}
.field{position:absolute;left:46px;width:396px;border:1px solid #cfcfcf;border-radius:2px;font-size:12px;color:#666;display:flex;align-items:center;gap:8px;padding-left:12px}
.field.message{align-items:flex-start;padding-top:14px;padding-left:18px}

/* footer */
.foot-brand{left:112px;top:3574px;font-family:"Syncopate",sans-serif;font-weight:700;font-size:22px;color:var(--white);letter-spacing:1px}
.social{left:183px;top:3661px;display:flex;gap:7px}
.social i{width:28px;height:28px;border-radius:50%;background:var(--white);display:block}
.col h5{font-size:13px;font-weight:700;color:var(--white);text-transform:uppercase;letter-spacing:.5px}
.col a{display:block;font-size:11.5px;color:#cfcfcf;text-decoration:none;margin-top:15px}
.col-bar{width:3px;height:26px;background:var(--white)}
.divider{width:1px;height:290px;background:#3a3b3e}
.copyright{left:0;top:3796px;width:1200px;height:70px;background:var(--footer-bottom);color:#bbb;font-size:10.5px;display:flex;align-items:center;justify-content:center}
</style>
</head>
<body>

<svg class="backdrop" viewBox="0 0 1200 3866" aria-hidden="true">
  <defs>
    <linearGradient id="heroBg" x1="0" y1="0" x2="0" y2="1">
      <stop offset="0" stop-color="#f6f7fb"/><stop offset="1" stop-color="#eef0f7"/>
    </linearGradient>
    <linearGradient id="redBand" x1="0" y1="0" x2="1" y2="1">
      <stop offset="0" stop-color="#b30025"/><stop offset="1" stop-color="#c9102f"/>
    </linearGradient>
  </defs>
  <!-- hero -->
  <rect x="0" y="0" width="1200" height="720" fill="url(#heroBg)"/>
  <path d="M0,560 Q560,800 1200,560 L1200,740 L0,740 Z" fill="#fff"/>
  <path d="M0,545 Q560,790 1200,565" fill="none" stroke="var(--red)" stroke-width="13"/>
  <path d="M925,520 L1200,572 L1196,588 L945,545 Z" fill="var(--red)"/>
  <!-- intelligence band -->
  <path d="M610,1263 Q950,1262 1200,1310" fill="none" stroke="#2b0b12" stroke-width="5"/>
  <path d="M0,1340 Q560,1230 1200,1325 L1200,1830 Q560,1950 0,1830 Z" fill="url(#redBand)"/>
  <path d="M0,1820 Q300,1905 620,1905" fill="none" stroke="var(--red-deep)" stroke-width="8"/>
  <!-- why choose band -->
  <path d="M0,2410 Q560,2290 1200,2380 L1200,2900 Q560,3000 0,2880 Z" fill="var(--grey-band)"/>
  <path d="M640,2322 Q960,2320 1200,2368" fill="none" stroke="var(--red)" stroke-width="7"/>
  <path d="M0,2882 Q300,2965 620,2968" fill="none" stroke="var(--red)" stroke-width="8"/>
  <!-- rings -->
  <circle cx="842" cy="1570" r="232" fill="#ffffff" fill-opacity="0.12"/>
  <circle cx="842" cy="1570" r="216" fill="#ffffff" fill-opacity="0.15"/>
  <circle cx="364" cy="2680" r="223" fill="none" stroke="#e3a7b3" stroke-width="1.5"/>
  <circle cx="364" cy="2680" r="207" fill="none" stroke="#e3a7b3" stroke-width="1.5"/>
  <circle cx="244" cy="2478" r="5" fill="var(--red)"/>
  <circle cx="521" cy="2783" r="5" fill="var(--red)"/>
  <!-- footer -->
  <rect x="0" y="3496" width="1200" height="300" fill="var(--footer)"/>
</svg>

<!-- header -->
<div class="abs brand">QVLT MERIDIAN</div>
<nav class="abs nav">
  <a class="active" href="#">About</a><a href="#">Services</a><a href="#">Technology</a><a href="#">Analytics</a><a href="#">Blogs</a>
</nav>
<a class="abs btn btn-solid nav-cta" href="#">Contact Us</a>

<!-- hero -->
<div class="abs arrow" style="left:34px;top:332px">‹</div>
<div class="abs arrow" style="left:1146px;top:332px">›</div>
<h1 class="abs display" style="left:110px;top:230px;font-size:36px;color:var(--ink)">
  <b>Intelligence</b><br><span>Analysis and</span><br><span style="color:var(--red)">Technology</span>
</h1>
<p class="abs para" style="left:110px;top:360px;width:370px">Lorem ipsum dolor sit amet, consectetur adipiscing elit, sed do eiusmod tempor incididunt ut labore.</p>
<a class="abs btn btn-solid" style="left:111px;top:424px;width:166px;height:46px" href="#">Explore More</a>
<div class="abs art" role="img" aria-label="Isometric illustration of a laptop showing data charts surrounded by glowing data cubes" style="left:540px;top:140px;width:610px;height:380px;background:radial-gradient(ellipse at 55% 45%,#cfe6f7 0%,#e4ecf8 45%,rgba(240,242,248,0) 75%)"></div>

<!-- about -->
<div class="abs art" role="img" aria-label="Isometric illustration of an analyst beside a large laptop displaying analytics charts" style="left:0;top:735px;width:560px;height:505px;background:radial-gradient(ellipse at 45% 40%,#cfd9f5 0%,#e8ecf8 45%,rgba(255,255,255,0) 75%)"></div>
<h2 class="abs display" style="left:648px;top:820px;font-size:30px;color:var(--ink)">
  <span style="color:var(--red)">About</span><br><span>QVLT</span> <b>Meridian</b>
</h2>
<div class="abs rule" style="left:649px;top:897px"></div>
<p class="abs para" style="left:650px;top:922px;width:440px">Lorem ipsum dolor sit amet, consectetur adipiscing elit, sed do eiusmod tempor incididunt ut labore et dolore magna aliqua. Ut enim ad minim veniam, quis nostrud exercitation</p>
<p class="abs para" style="left:650px;top:1005px;width:440px">Allamco laLorem ipsum dolor sit amet, consectetur adipiscing elit, sed do eiusmod tempor incididunt ut labore et dolore magna aliqua. Ut enim ad minim veniam, quis nostrud</p>
<a class="abs btn btn-outline" style="left:647px;top:1108px;width:160px;height:44px" href="#">Learn More</a>

<!-- intelligence analysis -->
<h2 class="abs display" style="left:135px;top:1425px;font-size:30px;color:var(--white)">
  <span>Intelligence</span><br><b>Analysis</b>
</h2>
<div class="abs rule" style="left:136px;top:1494px;background:var(--white)"></div>
<p class="abs para" style="left:134px;top:1520px;width:430px;color:#fff;font-size:16px;line-height:25px">Lorem ipsum dolor sit amet, consectetur adipiscing elit, sed do eiusmod tempor incididunt ut</p>
<p class="abs para" style="left:134px;top:1583px;width:430px;color:#fff;font-size:16px;line-height:25px">Ut enim ad minim veniam, quis nostrud exercitation ul-lamco laboris nisi ut aliquip ex ea commodo consequat. Duis aute irure dolor in reprehenderit in volup</p>
<a class="abs btn btn-ghost" style="left:131px;top:1685px;width:159px;height:43px" href="#">Learn More</a>
<div class="abs" role="img" aria-label="Isometric illustration of a gear and circuit platform for data processing" style="left:650px;top:1378px;width:384px;height:384px;border-radius:50%;background:radial-gradient(circle at 50% 50%,#ffffff 0%,#eef1fb 55%,#dfe6f6 100%)"></div>

<!-- technology -->
<h2 class="abs display" style="left:0;top:1983px;width:1200px;text-align:center;font-size:28px;color:var(--ink)"><span>Our</span> <b>Technology</b></h2>
<div class="abs rule" style="left:574px;top:2021px"></div>
<p class="abs para" style="left:240px;top:2036px;width:720px;text-align:center;font-size:15px;line-height:25px">Lorem ipsum dolor sit amet, consectetur adipiscing elit, sed do eiusmod tempor incididunt ut Ut enim ad minim veniam, quis nostrud exercitation ullamco laboris nisi ut aliquip ex</p>
<div class="abs feature" style="left:123px;top:2142px">
  <div class="icon" role="img" aria-label="Monitoring dashboard icon" style="background:var(--red)"></div>
  <div><h4>Lorem ipsum dolor</h4><p>Consectetur adipiscing elit sed do eius-mod tempor incididunt ut.</p></div>
</div>
<div class="abs feature" style="left:452px;top:2142px">
  <div class="icon" role="img" aria-label="Innovation idea icon" style="background:#a3a3a3"></div>
  <div><h4>Lorem ipsum dolor</h4><p>Consectetur adipiscing elit sed do eius-mod tempor incididunt ut.</p></div>
</div>
<div class="abs feature" style="left:777px;top:2142px">
  <div class="icon" role="img" aria-label="Analysis settings icon" style="background:#3e3e3e"></div>
  <div><h4>Lorem ipsum dolor</h4><p>Consectetur adipiscing elit sed do eius-mod tempor incididunt ut.</p></div>
</div>

<!-- why choose -->
<div class="abs" role="img" aria-label="Isometric illustration of a digital globe projected above a data server" style="left:172px;top:2488px;width:384px;height:384px;border-radius:50%;background:radial-gradient(circle at 50% 45%,#d5ecfb 0%,#eef3fb 55%,#f8f9fc 100%)"></div>
<h2 class="abs display" style="left:634px;top:2500px;font-size:30px;color:var(--ink)">
  <span>Why Choose</span><br><b style="color:var(--red)">QVLT Meridian</b>
</h2>
<div class="abs rule" style="left:635px;top:2571px"></div>
<p class="abs para" style="left:632px;top:2596px;width:450px;font-size:15px;line-height:25px">Lorem ipsum dolor sit amet, consectetur adipiscing elit, sed do eiusmod tempor incididunt ut</p>
<p class="abs para" style="left:632px;top:2659px;width:450px;font-size:15px;line-height:25px">Ut enim ad minim veniam, quis nostrud exercitation ullamco laboris nisi ut aliquip ex ea commodo consequat. Duis aute irure dolor in reprehenderit in voluptate velit esse cillum dolore eu fugiat nulla s nostrud exercitation ullamco laboris</p>
<a class="abs btn btn-outline" style="left:630px;top:2783px;width:159px;height:44px" href="#">Learn More</a>

<!-- contact -->
<p class="abs display" style="left:145px;top:3049px;font-size:12px;color:#666;letter-spacing:0">Get in Touch</p>
<h2 class="abs display" style="left:145px;top:3072px;font-size:30px;color:var(--ink)">
  <span style="color:var(--red)">Contact QVLT</span><br><b>Meridian LLC</b>
</h2>
<div class="abs rule" style="left:146px;top:3149px"></div>
<div class="abs contact-item" style="left:141px;top:3177px">
  <div class="ring"><svg width="26" height="26" viewBox="0 0 24 24" fill="none" stroke="var(--red)" stroke-width="1.6"><path d="M5 3h4l2 5-3 2a12 12 0 0 0 6 6l2-3 5 2v4a2 2 0 0 1-2 2A18 18 0 0 1 3 5a2 2 0 0 1 2-2z"/></svg></div>
  <div><small>Phone Number</small><strong>(+958) 5550 2719</strong></div>
</div>
<div class="abs contact-item" style="left:141px;top:3259px">
  <div class="ring"><svg width="28" height="22" viewBox="0 0 28 20" fill="none" stroke="var(--red)" stroke-width="1.8"><rect x="1" y="1" width="26" height="18" rx="2"/><path d="M1 2l13 10 13-10"/></svg></div>
  <div><small>Email address</small><strong>info@qvltmeridian.com</strong></div>
</div>

<form class="abs form">
  <div class="field" style="top:42px;height:44px"><svg width="14" height="14" viewBox="0 0 14 14" fill="none" stroke="#999"><circle cx="7" cy="4.5" r="3"/><path d="M1.5 13c1-3 3-4.5 5.5-4.5s4.5 1.5 5.5 4.5"/></svg>Name</div>
  <div class="field" style="top:98px;height:44px"><svg width="15" height="11" viewBox="0 0 15 11" fill="none" stroke="#999"><rect x=".5" y=".5" width="14" height="10"/><path d="M.5 1l7 5 7-5"/></svg>Email address</div>
  <div class="field" style="top:150px;height:42px"><svg width="13" height="13" viewBox="0 0 24 24" fill="none" stroke="#999" stroke-width="2"><path d="M5 3h4l2 5-3 2a12 12 0 0 0 6 6l2-3 5 2v4a2 2 0 0 1-2 2A18 18 0 0 1 3 5a2 2 0 0 1 2-2z"/></svg>Phone Number</div>
  <div class="field message" style="top:200px;height:85px">Message</div>
  <div class="btn btn-solid" style="position:absolute;left:47px;top:300px;width:153px;height:44px">Submit Now</div>
</form>

<!-- footer -->
<div class="abs foot-brand">QVLT MERIDIAN</div>
<div class="abs social" role="img" aria-label="Social media links"><i></i><i></i><i></i><i></i></div>
<div class="abs divider" style="left:408px;top:3500px"></div>
<div class="abs divider" style="left:640px;top:3500px"></div>
<div class="abs divider" style="left:864px;top:3500px"></div>
<div class="abs col-bar" style="left:406px;top:3566px"></div>
<div class="abs col-bar" style="left:638px;top:3566px"></div>
<div class="abs col-bar" style="left:862px;top:3566px"></div>
<div class="abs col" style="left:455px;top:3571px">
  <h5>Navigation</h5><a href="#">About Us</a><a href="#">Our Services</a><a href="#">Why We Are</a><a href="#">Projects</a>
</div>
<div class="abs col" style="left:687px;top:3571px">
  <h5>Resources</h5><a href="#">Terms &amp; Condition</a><a href="#">Privacy Policy</a><a href="#">Blogs</a><a href="#">Contact Us</a>
</div>
<div class="abs col" style="left:900px;top:3571px">
  <h5>Contact Us</h5>
</div>
<div class="abs" style="left:896px;top:3606px;display:flex;gap:10px;align-items:center">
  <svg width="26" height="26" viewBox="0 0 24 24" fill="none" stroke="var(--red)" stroke-width="1.6"><path d="M5 3h4l2 5-3 2a12 12 0 0 0 6 6l2-3 5 2v4a2 2 0 0 1-2 2A18 18 0 0 1 3 5a2 2 0 0 1 2-2z"/></svg>
  <div><div style="font-size:10px;color:#aaa">Phone Number</div><div style="font-size:12px;color:#fff">(+958) 5550 2719</div></div>
</div>
<div class="abs" style="left:896px;top:3660px;display:flex;gap:10px;align-items:center">
  <svg width="28" height="20" viewBox="0 0 28 20" fill="none" stroke="var(--red)" stroke-width="1.8"><rect x="1" y="1" width="26" height="18" rx="2"/><path d="M1 2l13 10 13-10"/></svg>
  <div><div style="font-size:10px;color:#aaa">Email address</div><div style="font-size:12px;color:#fff">info@qvltmeridian.com</div></div>
</div>
<div class="abs copyright">© 2022 QVLT Meridian &nbsp;|&nbsp; All Rights Reserved</div>

</body>
</html>
```